Commercial painting company is looking for a creative website designer.

Hi, we just completed our logo project and now ready to launch our website. The project will be done on Squarespace platform. It will contain:
Page 1 HOME
Page 2 SERVICES
Page 3 PICTURES
The content will be written by us. I am not sure bout the pictures, I do not have any to provide. I can buy stock photos if needed.
We are commercial only painting company and have to appeal to commercial, industrial property mangers. We will need CALL, REQUEST FOR ESTIMATE buttons.
If possible to have a live picture on home page would be great. Thank you
Target Market(s)
Property Managers
Industry/Entity Type
Commercial Painting
Other font styles liked:
- Poppins

```html
<!DOCTYPE html>
<html lang="en">
<head>
<meta charset="UTF-8">
<title>CoatLine Painters – Commercial Painting</title>
<link rel="stylesheet" href="https://fonts.googleapis.com/css2?family=Poppins:wght@400;500;600;700;800;900&display=swap">
<style>
:root{
  --red:#c10a30;
  --navy:#0c2a6b;
  --bg:#f6f6f6;
  --white:#ffffff;
  --text:#3a3a4a;
  --grey-photo-a:#7d7f88;
  --grey-photo-b:#c9ccd4;
}
*{box-sizing:border-box;margin:0;padding:0}
html,body{width:1200px;height:3834px;overflow:hidden}
body{position:relative;background:var(--bg);font-family:'Poppins',sans-serif;color:var(--text)}
.abs{position:absolute}
a{color:inherit;text-decoration:none}

/* Hero */
.hero-bg{left:0;top:0;width:1200px;height:840px}
.brand{left:96px;top:30px;display:flex;align-items:center;gap:10px;color:var(--white);font-weight:700;font-size:20px}
.brand-dot{width:26px;height:26px;border-radius:50%;background:var(--white)}
.nav{left:449px;top:40px;display:flex;gap:19px;font-size:13px;font-weight:600;color:var(--white);text-transform:uppercase}
.nav-call{left:768px;top:32px;display:flex;align-items:center;gap:8px;color:var(--white);font-size:12.5px;font-weight:600;line-height:1.25}
.btn-estimate{left:908px;top:28px;width:201px;height:44px;background:var(--red);color:var(--white);font-size:13.5px;font-weight:700;display:flex;align-items:center;justify-content:center}
.hero-welcome{left:90px;top:180px;font-size:27px;font-weight:700;color:var(--white)}
.hero-title{left:88px;top:218px;font-size:79px;line-height:75px;font-weight:800;color:var(--white);text-transform:uppercase;letter-spacing:-0.5px}
.hero-sub{left:90px;top:442px;font-size:20px;color:var(--white)}
.btn-discover{left:89px;top:489px;width:218px;height:63px;border:2px solid var(--white);color:var(--white);font-weight:700;font-size:18px;display:flex;align-items:center;justify-content:center}

/* About */
.about-photo{left:195px;top:972px;width:396px;height:396px;background:linear-gradient(135deg,#e7e8ec,#c6c9d3 60%,#3d4fa3)}
.about-title{left:626px;top:1030px;font-size:36px;font-weight:800;color:var(--navy)}
.about-text{left:626px;top:1081px;width:386px;font-size:13.4px;line-height:20.4px;color:var(--text)}
.btn-read{left:626px;top:1260px;width:116px;height:35px;background:var(--red);color:var(--white);font-size:11px;font-weight:700;display:flex;align-items:center;justify-content:center}

/* Services */
.services-band{left:0;top:1430px;width:1200px;height:600px}
.painter-figure{left:0;top:1520px;width:166px;height:695px;background:linear-gradient(180deg,#f1f1f1 0%,#2b56c8 35%,#1d3d9a 100%);border-radius:30px 40px 10px 10px}
.services-title{left:0;top:1562px;width:1200px;text-align:center;font-size:34px;font-weight:800;color:var(--white)}
.service-card{top:1631px;width:247px;height:247px;background:var(--white);display:flex;flex-direction:column;align-items:center;justify-content:flex-end;padding-bottom:34px;gap:16px}
.service-card span{font-size:21px;font-weight:700;color:var(--navy);text-transform:uppercase}

/* Gallery */
.gallery-title{left:0;top:2152px;width:1200px;text-align:center;font-size:35px;font-weight:800;color:var(--navy)}
.gallery-filter{left:0;top:2210px;width:1200px;display:flex;justify-content:center;gap:16px;font-size:18px;color:var(--navy)}
.gallery-filter .active{color:var(--red);font-weight:700}
.gallery-filter .sep{color:var(--navy)}
.gallery-item{}
.g1{left:89px;top:2264px;width:594px;height:306px;background:linear-gradient(135deg,#9ba4bf,#6d7aa3 55%,#1f3f8a)}
.g2{left:695px;top:2264px;width:416px;height:306px;background:linear-gradient(120deg,#e6e3dc,#f2f2f4 45%,#2e5bd1 60%,#cfe0ef)}
.g3{left:89px;top:2584px;width:334px;height:244px;background:linear-gradient(180deg,#7e95c4,#d9c6a9 45%,#e6dccb)}
.g4{left:432px;top:2584px;width:334px;height:244px;background:linear-gradient(110deg,#f2d54b,#f0e6b8 45%,#4f6aa8 60%,#e9e9e9)}
.g5{left:777px;top:2584px;width:334px;height:244px;background:linear-gradient(180deg,#e9e8e4,#cfcac0 60%,#e6d9be)}

/* Testimonials */
.testi-title{left:0;top:2900px;width:1200px;text-align:center;font-size:35px;font-weight:700;color:var(--navy)}
.avatar{border-radius:50%}
.av1{left:427px;top:2980px;width:98px;height:98px;background:linear-gradient(180deg,#8fa0c0,#2f3850)}
.av2{left:541px;top:2970px;width:118px;height:118px;background:linear-gradient(180deg,#d5d9e2,#20252f)}
.av3{left:675px;top:2980px;width:98px;height:98px;background:linear-gradient(180deg,#7fa3cd,#30578f)}
.quote-mark{left:0;top:3095px;width:1200px;text-align:center;font-size:70px;font-weight:900;color:var(--navy);line-height:70px}
.testi-text{left:225px;top:3152px;width:750px;text-align:center;font-size:14.6px;line-height:20px;color:var(--text)}
.testi-name{left:0;top:3218px;width:1200px;text-align:center;font-size:16px;font-weight:700;color:var(--red)}
.testi-stars{left:0;top:3240px;width:1200px;display:flex;justify-content:center;gap:1px}

/* Footer */
.footer-band{left:0;top:3360px;width:1200px;height:474px}
.footer-brand{left:177px;top:3530px;width:150px;height:150px;border-radius:50%;background:var(--white);display:flex;align-items:center;justify-content:center;text-align:center;font-size:19px;font-weight:700;color:var(--red);line-height:1.15}
.social{top:3704px;width:26px;height:26px;border-radius:50%;border:1px solid rgba(255,255,255,.5);background:rgba(255,255,255,.08)}
.footer-col h4{font-size:17px;font-weight:700;color:var(--white);margin-bottom:14px}
.footer-col{color:var(--white);font-size:12px}
.footer-col ul{list-style:none}
.footer-col li{margin-bottom:8px}
.contact-row{display:flex;gap:10px;align-items:flex-start;margin-bottom:10px;line-height:16px}
.newsletter-input{margin-top:16px;width:242px;height:40px;background:rgba(255,255,255,.12);display:flex;align-items:center;justify-content:space-between;padding:0 14px;font-size:12px;font-weight:500}
.footer-line{left:92px;top:3780px;width:1016px;height:1px;background:rgba(255,255,255,.3)}
.copyright{left:0;top:3800px;width:1200px;text-align:center;font-size:12px;font-weight:600;color:var(--white)}
.to-top{left:1117px;top:3763px;width:40px;height:40px;border-radius:50%;background:#173a85;display:flex;align-items:center;justify-content:center}
</style>
</head>
<body>

<!-- Hero -->
<svg class="abs hero-bg" viewBox="0 0 1200 840" role="img" aria-label="Photo of a painter in a blue cap rolling white paint on a ceiling beside protective plastic sheeting">
  <defs>
    <linearGradient id="heroGrad" x1="0" y1="0" x2="1" y2="1">
      <stop offset="0" stop-color="#6f717a"/>
      <stop offset="0.45" stop-color="#a8abb3"/>
      <stop offset="0.7" stop-color="#d9dbe0"/>
      <stop offset="1" stop-color="#3f7fd0"/>
    </linearGradient>
  </defs>
  <path fill="url(#heroGrad)" d="M0 0H1200V660L1180 700 1150 690 1110 720 1080 690 1040 700 1000 690 960 710 920 700 880 720 840 705 800 720 760 700 720 740 680 720 640 760 600 780 560 800 540 830 500 820 460 810 420 830 380 790 340 800 300 770 260 780 220 760 180 780 140 760 100 770 60 740 20 750 0 730Z"/>
</svg>

<div class="abs brand"><span class="brand-dot"></span>CoatLine Painters</div>
<nav class="abs nav"><a>Home</a><a>About us</a><a>Services</a><a>Gallery</a></nav>
<div class="abs nav-call">
  <svg width="16" height="18" viewBox="0 0 24 24"><path fill="#c10a30" d="M6.6 10.8a15.1 15.1 0 0 0 6.6 6.6l2.2-2.2c.3-.3.7-.4 1-.2 1.1.4 2.3.6 3.6.6.6 0 1 .4 1 1V20c0 .6-.4 1-1 1A17 17 0 0 1 3 4c0-.6.4-1 1-1h3.5c.6 0 1 .4 1 1 0 1.3.2 2.5.6 3.6.1.3 0 .7-.2 1z"/></svg>
  <div>CALL<br>0100.555.0199</div>
</div>
<a class="abs btn-estimate">REQUEST FOR ESTIMATE</a>

<div class="abs hero-welcome">WELCOME TO</div>
<h1 class="abs hero-title">Commercial<br>Only Paining<br>Company</h1>
<p class="abs hero-sub">appeal to commercial, industrial property mangers</p>
<a class="abs btn-discover">DISCOVER MORE</a>

<svg class="abs" style="left:545px;top:665px" width="115" height="50" viewBox="0 0 115 50">
  <line x1="0" y1="20" x2="28" y2="20" stroke="#fff" stroke-width="2"/>
  <line x1="87" y1="20" x2="115" y2="20" stroke="#fff" stroke-width="2"/>
  <rect x="38" y="3" width="38" height="14" rx="3" fill="none" stroke="#fff" stroke-width="2"/>
  <line x1="57" y1="17" x2="57" y2="30" stroke="#fff" stroke-width="2"/>
  <rect x="53" y="30" width="8" height="16" rx="3" fill="none" stroke="#fff" stroke-width="2"/>
</svg>

<!-- About -->
<div class="abs about-photo" role="img" aria-label="Photo of a painter in a red cap and blue overalls rolling paint on a white wall next to a ladder"></div>
<h2 class="abs about-title">ABOUT PAINTERS</h2>
<p class="abs about-text">It is a long established fact that a reader will be by the readable content of a page when looking at its layout. The point of using Lorem Ipsum is that it has a more-or-less normal distribution of letters, as op-posed to using 'Content here, content here', making it look like readable English. Many desktop publishing packages and web page editors now use Lorem Ipsum as their default model text...</p>
<a class="abs btn-read">READ MORE</a>

<!-- Services -->
<svg class="abs services-band" viewBox="0 0 1200 600">
  <path fill="var(--red)" d="M180 90 200 40 240 60 280 30 300 8 320 30 380 20 440 40 500 30 560 50 620 20 640 10 680 40 720 30 780 40 840 20 900 45 960 30 1020 40 1080 30 1120 20 1150 40 1180 10 1200 5V540L1170 545 1130 530 1100 560 1060 545 1000 530 940 550 880 540 820 555 760 535 720 560 680 540 640 575 600 560 560 590 520 570 480 560 440 575 400 550 360 560 340 540 300 550 260 535 200 545 150 530 120 500 140 440 120 380 140 300 110 220 130 150Z"/>
</svg>
<div class="abs painter-figure" role="img" aria-label="Illustration of a painter in a blue hard hat and overalls holding a paint roller"></div>
<h2 class="abs services-title">OUR SERVICES</h2>

<div class="abs service-card" style="left:212px">
  <svg width="116" height="130" viewBox="0 0 116 130" fill="none" stroke="var(--navy)" stroke-width="5">
    <rect x="6" y="40" width="36" height="86"/><rect x="42" y="10" width="36" height="116"/><rect x="78" y="30" width="32" height="96"/>
    <path d="M52 10V2h16v8" />
    <g stroke-width="4"><path d="M14 54h6M28 54h6M14 68h6M28 68h6M14 82h6M28 82h6M50 26h6M64 26h6M50 40h6M64 40h6M50 54h6M64 54h6M50 68h6M64 68h6M86 46h6M100 46h6M86 60h6M100 60h6M86 74h6M100 74h6"/>
    <path d="M54 126V96h12v30M90 126V96M98 126V96"/></g>
  </svg>
  <span>Commercial</span>
</div>
<div class="abs service-card" style="left:477px">
  <svg width="130" height="130" viewBox="0 0 130 130" fill="none" stroke="var(--navy)" stroke-width="5">
    <path d="M6 56 60 10l54 46"/><path d="M18 46v80h70V46"/><path d="M88 80h36v46H88"/>
    <rect x="48" y="30" width="24" height="14"/>
    <g stroke-width="4"><rect x="28" y="56" width="16" height="14"/><rect x="52" y="56" width="26" height="14"/><rect x="28" y="82" width="20" height="16"/><rect x="98" y="90" width="16" height="14"/><path d="M58 126V98h18v28M24 116h60M94 116h26"/></g>
  </svg>
  <span>Residential</span>
</div>
<div class="abs service-card" style="left:741px">
  <svg width="132" height="130" viewBox="0 0 132 130" fill="none" stroke="var(--navy)" stroke-width="5">
    <path d="M4 60 52 16l48 44"/><path d="M16 50v40M88 50v22"/>
    <path d="M96 4v18M87 13h18M26 14v12M20 20h12" stroke-width="4"/>
    <polygon points="30,82 44,74 58,82 58,98 44,106 30,98"/>
    <circle cx="44" cy="90" r="6"/>
    <path d="M58 90h40l10-12h16l-10 14 10 12h-16l-10-12"/>
  </svg>
  <span>Restoration</span>
</div>

<!-- Gallery -->
<h2 class="abs gallery-title">GALLERY</h2>
<div class="abs gallery-filter"><span class="active">ALL</span><span class="sep">|</span><span>RESTORATION</span><span class="sep">&nbsp;|&nbsp;</span><span>RESIDENTIAL</span><span class="sep">|</span><span>&nbsp;COMMERCIAL</span></div>
<div class="abs gallery-item g1" role="img" aria-label="Photo of a painter on a rope painting a building facade above large windows"></div>
<svg class="abs" style="left:369px;top:2404px" width="32" height="32" viewBox="0 0 32 32" fill="none" stroke="var(--red)" stroke-width="4"><circle cx="13" cy="13" r="9"/><path d="M20 20l9 9"/></svg>
<div class="abs gallery-item g2" role="img" aria-label="Photo of a painter in white crouching to roll paint on a wall beside a ladder"></div>
<div class="abs gallery-item g3" role="img" aria-label="Photo of a painter working on a house window under a blue sky"></div>
<div class="abs gallery-item g4" role="img" aria-label="Photo of a painter in a blue hard hat rolling yellow paint on a wall"></div>
<div class="abs gallery-item g5" role="img" aria-label="Photo of an empty office corridor under renovation"></div>

<!-- Testimonials -->
<h2 class="abs testi-title">Testimonials</h2>
<div class="abs avatar av1" role="img" aria-label="Client portrait"></div>
<div class="abs avatar av2" role="img" aria-label="Client portrait"></div>
<div class="abs avatar av3" role="img" aria-label="Client portrait"></div>
<div class="abs quote-mark">&ldquo;</div>
<p class="abs testi-text">is simply dummy text of the printing and typesetting industry. Lorem Ipsum has been the industry's stan-dard dummy text ever since the 1500s, when an unknown printer took a galley of type and scrambled it to make a type specimen book. It has survived not only five centuries,</p>
<div class="abs testi-name">Dana Reyes</div>
<div class="abs testi-stars">
  <svg width="64" height="12" viewBox="0 0 64 12" fill="#e0a31c"><g id="st"><path d="M6 0l1.8 3.9 4.2.4-3.2 2.8.9 4.1L6 9.1 2.3 11.2l.9-4.1L0 4.3l4.2-.4z"/></g><use href="#st" x="13"/><use href="#st" x="26"/><use href="#st" x="39"/><use href="#st" x="52"/></svg>
</div>

<!-- Footer -->
<svg class="abs footer-band" viewBox="0 0 1200 474">
  <path fill="var(--navy)" d="M0 22 40 30 80 20 120 0 150 30 200 20 260 30 320 40 380 25 420 12 460 30 520 20 580 40 620 10 660 30 700 20 760 35 820 25 880 30 940 10 990 30 1040 20 1100 35 1150 20 1200 10V474H0Z"/>
</svg>
<div class="abs footer-brand">CoatLine<br>Painters</div>
<div class="abs social" style="left:205px"></div>
<div class="abs social" style="left:240px"></div>
<div class="abs social" style="left:275px"></div>

<div class="abs footer-col" style="left:440px;top:3562px">
  <h4>Quick Link</h4>
  <ul><li>home</li><li>about us</li><li>services</li><li>gallery</li></ul>
</div>
<div class="abs footer-col" style="left:592px;top:3562px;width:200px">
  <h4>Contact Us</h4>
  <div class="contact-row"><svg width="10" height="12" viewBox="0 0 10 12"><path fill="var(--red)" d="M5 0a4 4 0 0 1 4 4c0 3-4 8-4 8S1 7 1 4a4 4 0 0 1 4-4z"/><circle cx="5" cy="4" r="1.5" fill="var(--navy)"/></svg><span>12 Sample Lane,<br>Exampleton AB1 2CD</span></div>
  <div class="contact-row"><svg width="12" height="12" viewBox="0 0 24 24"><path fill="var(--red)" d="M6.6 10.8a15.1 15.1 0 0 0 6.6 6.6l2.2-2.2c.3-.3.7-.4 1-.2 1.1.4 2.3.6 3.6.6.6 0 1 .4 1 1V20c0 .6-.4 1-1 1A17 17 0 0 1 3 4c0-.6.4-1 1-1h3.5c.6 0 1 .4 1 1 0 1.3.2 2.5.6 3.6.1.3 0 .7-.2 1z"/></svg><span>0100.555.0199</span></div>
  <div class="contact-row"><svg width="12" height="10" viewBox="0 0 12 10"><rect width="12" height="10" fill="var(--red)"/><path d="M0 0l6 5 6-5" stroke="var(--navy)" fill="none"/></svg><span>hello@coatline.test</span></div>
</div>
<div class="abs footer-col" style="left:818px;top:3562px;width:250px">
  <h4>Newsletter</h4>
  <p style="line-height:18px">It is a long established fact that a<br>reader will be distracted .</p>
  <div class="newsletter-input"><span>&#9993;&nbsp; Enter email address</span>
    <svg width="14" height="14" viewBox="0 0 14 14"><path fill="var(--red)" d="M0 6 14 0 8 14 6 8z"/></svg></div>
</div>
<div class="abs footer-line"></div>
<div class="abs copyright">© Copyright 2023 &nbsp;| All Right Reserveds</div>
<div class="abs to-top"><svg width="10" height="8" viewBox="0 0 10 8"><path d="M1 6l4-4 4 4" stroke="#fff" stroke-width="1.6" fill="none"/></svg></div>

</body>
</html>
```